Lernoptic.com Business Card Design Project

We need a new business card design for our new online company that delivers online education. It initially focused on SEO training but will soon offer more. The design should be fresh and trendy and take into account the colors and website design attached.
Industry/Entity Type
Training

```html
<!DOCTYPE html>
<html lang="en">
<head>
<meta charset="utf-8">
<title>Lernoptic Business Card</title>
<link rel="stylesheet" href="https://fonts.googleapis.com/css2?family=Quicksand:wght@500&family=Arimo:wght@400;700&display=swap">
<style>
  :root {
    --brand-green: #077f45;
    --ink-grey: #6d6e70;
    --paper: #ffffff;
    --backdrop: #e6e7e8;
    --card-shadow: rgba(0, 0, 0, 0.18);
  }
  * { box-sizing: border-box; margin: 0; padding: 0; }
  html, body {
    width: 1067px;
    height: 1200px;
    overflow: hidden;
    background: var(--backdrop);
  }
  .sheet {
    position: relative;
    width: 1067px;
    height: 1200px;
  }
  .card {
    position: absolute;
    left: 153px;
    width: 760px;
    height: 434px;
    box-shadow: 0 6px 18px var(--card-shadow);
  }
  .card--front { top: 130px; background: var(--brand-green); }
  .card--back { top: 636px; background: var(--paper); }

  /* Front */
  .front-brand {
    position: absolute;
    left: 0; right: 0; top: 92px;
    display: flex;
    flex-direction: column;
    align-items: center;
    color: var(--paper);
  }
  .front-brand__mark {
    width: 96px;
    height: 96px;
    background: var(--paper);
    border-radius: 6px;
  }
  .front-brand__name {
    margin-top: 18px;
    font-family: "Quicksand", sans-serif;
    font-weight: 500;
    font-size: 84px;
    line-height: 1;
    letter-spacing: 1px;
  }
  .front-brand__url {
    margin-top: 6px;
    font-family: "Arimo", sans-serif;
    font-size: 15px;
    align-self: center;
    padding-left: 210px;
  }

  /* Back */
  .back-brand {
    position: absolute;
    left: 64px; top: 58px;
    display: flex;
    align-items: center;
    gap: 16px;
  }
  .back-brand__mark {
    width: 62px;
    height: 62px;
    background: var(--brand-green);
    border-radius: 4px;
  }
  .back-brand__name {
    font-family: "Quicksand", sans-serif;
    font-weight: 500;
    font-size: 68px;
    line-height: 1;
    color: var(--ink-grey);
  }
  .holder {
    position: absolute;
    right: 430px; top: 230px;
    text-align: right;
    font-family: "Arimo", sans-serif;
  }
  .holder__name {
    color: var(--brand-green);
    font-weight: 700;
    font-size: 21px;
  }
  .holder__role {
    color: var(--ink-grey);
    font-size: 15px;
    margin-top: 2px;
  }
  .holder__address {
    color: var(--ink-grey);
    font-size: 15px;
    line-height: 1.3;
    margin-top: 20px;
  }
  .divider {
    position: absolute;
    left: 348px; top: 222px;
    display: flex;
    gap: 4px;
    height: 92px;
  }
  .divider__bold { width: 8px; background: var(--brand-green); }
  .divider__thin { width: 2px; background: var(--ink-grey); }
  .contacts {
    position: absolute;
    left: 374px; top: 220px;
    list-style: none;
    font-family: "Arimo", sans-serif;
    font-size: 15px;
    line-height: 24px;
    color: var(--ink-grey);
  }
  .contacts__label {
    display: inline-block;
    width: 20px;
    color: var(--brand-green);
  }
</style>
</head>
<body>
<main class="sheet">
  <section class="card card--front" aria-label="Card front">
    <div class="front-brand">
      <div class="front-brand__mark"></div>
      <div class="front-brand__name">lernoptic</div>
      <div class="front-brand__url">www.lernoptic.com</div>
    </div>
  </section>

  <section class="card card--back" aria-label="Card back">
    <div class="back-brand">
      <div class="back-brand__mark"></div>
      <div class="back-brand__name">lernoptic</div>
    </div>

    <div class="holder">
      <p class="holder__name">Daniel Marsh</p>
      <p class="holder__role">Manager</p>
      <p class="holder__address">00000 Alder Crest Way,<br>Lake Mirren, FL 00000</p>
    </div>

    <div class="divider" aria-hidden="true">
      <span class="divider__bold"></span>
      <span class="divider__thin"></span>
    </div>

    <ul class="contacts">
      <li><span class="contacts__label">p:</span> 000 000 1111</li>
      <li><span class="contacts__label">f:</span> 000 000 1111</li>
      <li><span class="contacts__label">e:</span> info@lernoptic.com</li>
      <li><span class="contacts__label">w:</span> www.lernoptic.com</li>
    </ul>
  </section>
</main>
</body>
</html>
```